NZ First of it's kind solutions directory and marketplace for busy Mums needs a business card design

We need a business card design for our new nationwide business in NZ (long term plans to go global). We provide solutions to the everyday challenges that busy Mums face by connecting them with quality communities and suppliers of carefully selected, relevant products and services. We sell direct via our online marketplace. The final design should communicate our values of inclusivity, quality and smart solutions. Colours should incorporate our logo colour palette of #477077 and #6ba8b2. Our website is at https://www.brightnestly.com

Target Market(s)

busy Mums, Age 28 – 50, female, income over $100K, location main centres NZ primarily but NZ wide. Is likely juggling work or career with a young family. Probably had hobbies which have fallen by the wayside.
-Wants to succeed in her chosen career without compromising on family life
-to successfully juggle her career without feeling like she is compromising her children
- Is time poor, something always has to give and it’s generally her health (she’ll stay up late, get stressed)
- probably ex corporate or professional career. Has discretional income

Industry/Entity Type

Business

Contact Information for Business Card

Jodie Farnsworth, Founder, BrightNestly.com (Strapline Browse; Pick; Sorted), 48 Kowhai Terrace, Hillsborough, Auckland 1058, New Zealand. Mob: 021 437 518 Ph: +64 (0)9 584 7163

Font styles to use
Other font styles liked:
• Raleway, and/or Architects Daughter

Colors
00a990
33b8a4
86cfc6
cfeae6

Requirements
Must have
• the above details, streamline. the logo and colours associated with those logos
Should not have
• foil or metallic colours

```html
<!DOCTYPE html>
<html lang="en">
<head>
<meta charset="utf-8">
<title>BrightNestly Business Card</title>
<link rel="stylesheet" href="https://fonts.googleapis.com/css2?family=Jost:wght@400;500;600&display=swap">
<style>
  :root {
    --brand-dark: #477077;
    --brand-deep: #527479;
    --brand-light: #6ba8b2;
    --paper: #ffffff;
    --edge: #d9d9d9;
    --shadow-soft: #e6e6e6;
  }
  * { margin: 0; padding: 0; box-sizing: border-box; }
  html, body {
    width: 1200px;
    height: 1200px;
    overflow: hidden;
    background: var(--paper);
    font-family: "Jost", "Helvetica Neue", Arial, sans-serif;
  }
  .sheet { position: relative; width: 1200px; height: 1200px; }
  .card {
    position: absolute;
    left: 270px;
    width: 660px;
    height: 427px;
    border: 1.5px solid var(--edge);
    border-radius: 26px;
    background: var(--paper);
    overflow: hidden;
  }
  .card--front { top: 136px; }
  .card--back { top: 637px; }

  /* Front */
  .brand {
    position: absolute;
    left: 20px;
    top: 100px;
    display: flex;
    align-items: center;
    gap: 26px;
  }
  .brand__dot {
    width: 50px;
    height: 50px;
    border-radius: 50%;
    background: var(--brand-deep);
    flex: none;
  }
  .brand__name {
    font-size: 70px;
    font-weight: 600;
    color: var(--brand-deep);
    letter-spacing: -1px;
    line-height: 1;
  }
  .front__rule {
    position: absolute;
    left: 44px;
    right: 44px;
    top: 345px;
    height: 2px;
    background: var(--brand-deep);
  }
  .front__url {
    position: absolute;
    left: 0;
    right: 0;
    top: 363px;
    text-align: center;
    font-size: 24px;
    font-weight: 400;
    letter-spacing: 7px;
    color: var(--brand-light);
  }

  /* Back */
  .back__swoosh { position: absolute; inset: 0; width: 100%; height: 100%; }
  .person {
    position: absolute;
    left: 58px;
    top: 68px;
    color: var(--paper);
  }
  .person__name { font-size: 36px; font-weight: 400; line-height: 1.1; }
  .person__role {
    margin-left: 51px;
    font-size: 24px;
    font-weight: 400;
    letter-spacing: 2px;
    text-transform: uppercase;
    line-height: 1.2;
  }
  .contact {
    position: absolute;
    left: 58px;
    top: 232px;
    font-size: 23px;
    line-height: 29.5px;
    color: var(--brand-deep);
    font-style: normal;
  }
  .contact__label { color: var(--brand-light); }
  .back__mark {
    position: absolute;
    left: 503px;
    top: 222px;
    width: 120px;
    height: 120px;
    border-radius: 50%;
    background: var(--brand-deep);
  }
  .back__mark-shadow {
    position: absolute;
    left: 506px;
    top: 366px;
    width: 114px;
    height: 18px;
    border-radius: 50%;
    background: var(--shadow-soft);
  }
</style>
</head>
<body>
<main class="sheet">
  <section class="card card--front" aria-label="Card front">
    <div class="brand">
      <span class="brand__dot"></span>
      <span class="brand__name">BrightNestly</span>
    </div>
    <div class="front__rule"></div>
    <p class="front__url">WWW.BRIGHTNESTLY.COM</p>
  </section>

  <section class="card card--back" aria-label="Card back">
    <svg class="back__swoosh" viewBox="0 0 550 356" preserveAspectRatio="none" aria-hidden="true">
      <path d="M0 0 H545 C470 95 300 168 0 136 Z" fill="var(--brand-deep)"/>
      <path d="M0 146 C300 176 480 100 545 4 C485 112 310 198 0 180 Z" fill="var(--brand-light)"/>
    </svg>
    <div class="person">
      <p class="person__name">Jodie Farnsworth</p>
      <p class="person__role">Founder</p>
    </div>
    <address class="contact">
      48 Kowhai Terrace,<br>
      Hillsborough, Auckland 1058,<br>
      New Zealand.<br>
      <span class="contact__label">Mob:</span> 021 437 518<br>
      <span class="contact__label">Ph:</span> +64 (0)9 584 7163
    </address>
    <span class="back__mark-shadow"></span>
    <span class="back__mark"></span>
  </section>
</main>
</body>
</html>
```